Book & e-book cover - front, back and sleeve

Please see plot description:

The Lantern

A man lies dying and trapped in a parking garage stairwell. The poorly lit stairwell serves as a painful reminder of one of his memories of childhood locked in that darkened closet. To keep himself in tact he would play with a shiny silver button he ripped off from his pajamas – throwing it in the air and tapping the floor to find it. As he lies trapped and dying that same defeated and abandoned feeling descends upon him. As he comes in and out of consciousness memories from his past manifest themselves and we are introduced to the turbulent and sometimes triumphant pathway that has led him to his current state. It is up to him to sort through the barrage of emotions to find his way out, to let go, to forgive. That is if his heart will let him.
Updates

I know that we mentioned having a photograph of a button on the cover but we would like to see examples of covers with a more abstract or drawn or painted looking button.  Thanks.

Target Market(s)

Dramatic story - geared towards adult readers

Industry/Entity Type

Parking

Requirements
Must have
• Simple, crisp, custom, classic look. Do not want it to look to sci-fi or medival - this is an emotional story - a memoir.

Items on the front cover:

Title: The Lantern
Author: R.L. Marsh
Words: A Novel
Photo: a sliver button (just one image)

Items on the back cover

Plot description area
ISBN area at bottom

Nice to have
• Please see examples that have been uploaded. I like novels with a textured background.

A simple button on the cover with the right fonts and colour scheme.
Should not have
• I do not want a person or icons used on the cover
I do not want it to busy.
Do not want it to feel like it is a sci-fi novel or medival story.
Do not want the cover to be too "dark" - I do not want potential readers to get the wrong idea of what "The Lantern" is about.

```html
<!DOCTYPE html>
<html lang="en">
<head>
<meta charset="utf-8">
<title>The Lantern – cover options</title>
<link rel="stylesheet" href="https://fonts.googleapis.com/css2?family=Inter:wght@200;300&display=swap">
<style>
  :root {
    --board-top: #f4f4f4;
    --board-bottom: #dcdcdc;
    --label-blue: #6a97bf;
    --cover-deep: #3f7299;
    --cover-mid: #6d9dc1;
    --cover-pale: #a8cdd6;
    --cover-mist: #8fb6cc;
    --type-white: #ffffff;
    --silver-light: #ecebe6;
    --silver-mid: #c4c3bb;
    --silver-dark: #8e8e88;
  }
  * { box-sizing: border-box; margin: 0; padding: 0; }
  html, body { width: 1200px; height: 764px; overflow: hidden; }
  body {
    position: relative;
    background: linear-gradient(180deg, var(--board-top) 0%, #e9e9e9 60%, var(--board-bottom) 100%);
    font-family: "Inter", "Helvetica Neue", Arial, sans-serif;
  }
  .option-label {
    position: absolute; top: 36px; width: 40px; margin-left: -20px;
    text-align: center; color: var(--label-blue);
    font-size: 18px; font-weight: 300; line-height: 22px;
  }
  .option-label svg { display: block; margin: 6px auto 0; }
  .cover {
    position: absolute; top: 100px; width: 395px; height: 592px; overflow: hidden;
    color: var(--type-white);
    background:
      radial-gradient(ellipse 55% 40% at 22% 28%, rgba(63,96,120,.75), transparent 70%),
      radial-gradient(ellipse 60% 45% at 78% 62%, rgba(184,218,222,.85), transparent 70%),
      radial-gradient(ellipse 50% 30% at 25% 88%, rgba(80,130,165,.7), transparent 70%),
      radial-gradient(ellipse 70% 25% at 50% 100%, rgba(60,110,150,.55), transparent 70%),
      linear-gradient(160deg, var(--cover-deep) 0%, var(--cover-mid) 35%, var(--cover-mist) 60%, var(--cover-pale) 75%, var(--cover-mid) 100%);
  }
  .cover--one { left: 0; }
  .cover--two { left: 403px; }
  .cover--three { left: 805px; }
  .title {
    position: absolute; top: 128px; left: 0; right: 0;
    text-align: center; font-weight: 200; line-height: 1;
  }
  .title-the {
    position: absolute; top: -19px; right: 106px;
    font-size: 36px; font-weight: 300; line-height: 1; letter-spacing: -0.5px;
  }
  .title-word { display: inline-block; font-size: 106px; letter-spacing: -2.5px; }
  .title-e { position: relative; color: transparent; }
  .button-disc {
    position: absolute; left: 50%; top: 68px;
    width: 76px; height: 76px; margin: -38px 0 0 -38px; border-radius: 50%;
    background: radial-gradient(circle at 40% 36%, var(--silver-light) 0%, var(--silver-mid) 58%, var(--silver-dark) 100%);
    box-shadow: 0 3px 7px rgba(30,50,70,.45);
  }
  .subtitle {
    position: absolute; top: 324px; left: 167px;
    font-size: 16px; font-weight: 300; letter-spacing: 2.2px;
  }
  .author {
    position: absolute; top: 514px; left: 0; right: 0; text-align: center;
    font-size: 32px; font-weight: 200; letter-spacing: 0.3px;
  }
</style>
</head>
<body>

  <div class="option-label" style="left:200px">1<svg width="10" height="12" viewBox="0 0 10 12"><path d="M5 0v11M1 7l4 4 4-4" fill="none" stroke="currentColor" stroke-width="1"/></svg></div>
  <div class="option-label" style="left:600px">2<svg width="10" height="12" viewBox="0 0 10 12"><path d="M5 0v11M1 7l4 4 4-4" fill="none" stroke="currentColor" stroke-width="1"/></svg></div>
  <div class="option-label" style="left:1002px">3<svg width="10" height="12" viewBox="0 0 10 12"><path d="M5 0v11M1 7l4 4 4-4" fill="none" stroke="currentColor" stroke-width="1"/></svg></div>

  <section class="cover cover--one">
    <h1 class="title"><span class="title-the">the</span><span class="title-word">lant<span class="title-e">e<span class="button-disc" role="img" aria-label="Worn silver button with a loose thread trailing across the cover"></span></span>rn</span></h1>
    <p class="subtitle">a novel</p>
    <p class="author">R.L. Marsh</p>
  </section>

  <section class="cover cover--two">
    <h1 class="title"><span class="title-the">the</span><span class="title-word">lant<span class="title-e">e<span class="button-disc" role="img" aria-label="Worn silver button with two loose threads trailing down the cover"></span></span>rn</span></h1>
    <p class="subtitle">a novel</p>
    <p class="author">R.L. Marsh</p>
  </section>

  <section class="cover cover--three">
    <h1 class="title"><span class="title-the">the</span><span class="title-word">lant<span class="title-e">e<span class="button-disc" role="img" aria-label="Cracked silver button with thread running above and below it"></span></span>rn</span></h1>
    <p class="subtitle">a novel</p>
    <p class="author">R.L. Marsh</p>
  </section>

</body>
</html>
```